Business card and insta posting square

This is for 2 separate projects...

1...a double sided business card for online business (no address) to hand to businesses to get them to list their details on my online directory. the butterfly logo is to be used on the business card.

2.... a posting square for Instagram to write inspirational quotes over the top of to post....with a small butterfly logo somewhere on it (in a corner maybe)....the square is to have a thin, solid green outline around the edge of it, and a faded picture through the background that will allow me to write text over the top of it that will be easily readable.
I would like the same box for all Instagram quote posts for consistency ..

Target Market(s)

spiritual , yoga, meditation, wellness......

Industry/Entity Type

Wellness

Contact Information for Business Card

Details for Business Card...
Wandering The Quiet Tide
Your Complete Wellness Directory
www.wanderingthequiettide.example
PICTA/FRENDLY/PINBOARD/CHIRP
*List Your Business for FREE *

Colors
33b8a4
34a7d8
3276b5
876aae
9bcb3c

Requirements
Must have
• butterfly logo included on business card
• insta post square can use the butterfly logo OR the WTQT green square uploaded in the images
Nice to have
• greens

```html
<!DOCTYPE html>
<html lang="en">
<head>
<meta charset="utf-8">
<title>Wandering The Quiet Tide – Business Card and Post Square</title>
<link rel="stylesheet" href="https://fonts.googleapis.com/css2?family=Source+Sans+3:wght@400;600;700&family=Roboto:wght@300&display=swap">
<style>
  :root {
    --canvas-bg: #e6e6e6;
    --card-white: #ffffff;
    --leaf-green: #5fa830;
    --band-green: #5fa830;
    --deep-purple: #521e85;
    --ink-green: #2f8a2f;
    --mint: #b3e3ab;
    --badge-green: #4aa64a;
    --butterfly-teal: #34a7d8;
    --butterfly-violet: #6a1f8f;
  }
  * { box-sizing: border-box; margin: 0; padding: 0; }
  html, body { width: 1200px; height: 848px; overflow: hidden; }
  body {
    background: var(--canvas-bg);
    position: relative;
    font-family: "Source Sans 3", "Helvetica Neue", Arial, sans-serif;
  }

  /* Business card – front */
  .card-front {
    position: absolute; left: 55px; top: 24px; width: 555px; height: 370px;
    background: var(--card-white);
    box-shadow: -6px 8px 18px rgba(0,0,0,0.18);
    overflow: hidden;
  }
  .card-front .butterfly-logo {
    position: absolute; left: 204px; top: 44px; width: 251px; height: 170px;
    background: radial-gradient(ellipse at 50% 55%, var(--butterfly-violet) 0%, #4b4fb0 45%, rgba(52,167,216,0.55) 70%, rgba(155,203,60,0) 100%);
    border-radius: 45% 45% 40% 40%;
  }
  .card-front .brand-name {
    position: absolute; left: 0; right: 0; top: 236px;
    text-align: center;
    font-weight: 400; font-size: 40px; color: var(--ink-green);
    letter-spacing: 0.5px;
  }
  .card-front .band-green {
    position: absolute; left: 0; right: 0; top: 318px; height: 8px;
    background: var(--band-green);
  }
  .card-front .band-purple {
    position: absolute; left: 0; right: 0; top: 326px; height: 44px;
    background: var(--deep-purple);
    display: flex; align-items: center; justify-content: center;
  }
  .card-front .web-address {
    color: #fff; font-weight: 700; font-size: 20px; letter-spacing: 0.2px;
  }

  /* Business card – back */
  .card-back {
    position: absolute; left: 51px; top: 432px; width: 555px; height: 370px;
    background: var(--leaf-green);
    box-shadow: 6px 8px 18px rgba(0,0,0,0.18);
  }
  .card-back .tagline-box {
    position: absolute; left: 84px; top: 126px; width: 405px; height: 73px;
    border: 1.5px solid #fff;
    display: flex; align-items: center; justify-content: center;
    color: #fff; font-weight: 700; font-size: 21px;
  }
  .card-back .contact-label {
    position: absolute; left: 49px; top: 272px;
    font-family: "Roboto", Arial, sans-serif; font-weight: 300;
    font-size: 26px; color: #fff; letter-spacing: 0.5px;
  }
  .card-back .contact-divider {
    position: absolute; left: 174px; top: 253px; width: 1.5px; height: 61px;
    background: var(--deep-purple);
  }
  .card-back .contact-lines {
    position: absolute; left: 190px; top: 248px;
    color: #fff; font-weight: 700; font-size: 19.5px; line-height: 34px;
  }

  /* Post square */
  .post-square {
    position: absolute; left: 687px; top: 232px; width: 456px; height: 456px;
    background: var(--mint);
  }
  .post-square .frame {
    position: absolute; left: 27px; top: 14px; width: 402px; height: 425px;
    border: 5px solid var(--deep-purple); border-radius: 10px;
  }
  .post-square .faded-butterfly {
    position: absolute; left: 65px; top: 128px; width: 332px; height: 222px;
    background: radial-gradient(ellipse at 50% 50%, rgba(110,160,120,0.45) 0%, rgba(120,190,150,0.3) 50%, rgba(179,227,171,0) 85%);
    border-radius: 45%;
  }
  .post-square .badge {
    position: absolute; left: 360px; top: 371px; width: 54px; height: 54px;
    border-radius: 50%; background: var(--badge-green);
    border: 2px solid #fff; box-shadow: 0 0 0 1px var(--badge-green);
    display: flex; align-items: center; justify-content: center;
    color: #fff; font-weight: 600; font-size: 15px;
  }
</style>
</head>
<body>
  <section class="card-front">
    <div class="butterfly-logo" role="img" aria-label="Butterfly illustration in violet and teal with small green butterflies"></div>
    <div class="brand-name">Wandering The Quiet Tide</div>
    <div class="band-green"></div>
    <div class="band-purple"><span class="web-address">www.wanderingthequiettide.example</span></div>
  </section>

  <section class="card-back">
    <div class="tagline-box">Your Complete Wellness Directory</div>
    <div class="contact-label">CONTACT</div>
    <div class="contact-divider"></div>
    <div class="contact-lines">
      <div>www.wanderingthequiettide.example</div>
      <div>PICTA/FRENDLY/PINBOARD/CHIRP</div>
    </div>
  </section>

  <section class="post-square">
    <div class="frame"></div>
    <div class="faded-butterfly" role="img" aria-label="Faded butterfly illustration in soft greens behind the quote area"></div>
    <div class="badge">wtqt</div>
  </section>
</body>
</html>
```